Income Tax and Accounting Brochure

I need a brochure using my new logo (file attached). I do tax work and accounting work. I am an EA (QDX Enrolled Agent - logo attached) and would like this incorporated into the brochure. I also have a MSA in Accounting. Please incorporate the text that I have provided in the brochure.

Target Market(s)

Tax Clients - both business and individuals

Industry/Entity Type

Accounting

Colors
0054AA
0677BA
7BADD7
CADEEF
E8F1F8

Requirements
Must have
• Use my logo and the QDX EA file in the brochure
Nice to have
• I would like to see a brochure that I can customize with my own text if possible.

```html
<!DOCTYPE html>
<html lang="en">
<head>
<meta charset="utf-8">
<title>MTH Accounting &amp; Consulting – Brochure Spread</title>
<link rel="stylesheet" href="https://fonts.googleapis.com/css2?family=Cinzel:wght@600;700&family=Montserrat:wght@400;500&display=swap">
<style>
  :root{
    --backdrop:#ecedf0;
    --paper:#ffffff;
    --royal:#0a4fb3;
    --deep-blue:#073f9c;
    --crimson:#c4143d;
    --wine:#8c0d22;
    --ink:#2a2a2a;
    --heading:#0c3f8f;
    --sub:#c4143d;
    --badge:#9a9a9a;
  }
  *{box-sizing:border-box;margin:0;padding:0}
  html,body{width:900px;height:1200px;overflow:hidden}
  body{background:var(--backdrop);position:relative;font-family:"Montserrat",sans-serif;color:var(--ink)}
  .page{position:absolute;top:295px;width:435px;height:610px;background:var(--paper);overflow:hidden;box-shadow:0 2px 10px rgba(0,0,0,.12)}
  .page--about{left:10px}
  .page--services{left:455px}
  .page__art{position:absolute;inset:0;width:100%;height:100%}
  .heading{font-family:"Cinzel",serif;font-weight:700;color:var(--heading);letter-spacing:.2px;border-bottom:1.5px solid #111;display:inline-block;padding-bottom:2px;white-space:nowrap}

  .about{position:absolute;left:0;right:0;top:222px;text-align:center}
  .about .heading{font-size:14.5px}
  .about__text{font-size:10.4px;line-height:1.42;margin:14px 36px 0 36px}
  .about__text+.about__text{margin-top:12px}

  .brand-row{position:absolute;top:440px;left:66px;display:flex;align-items:center;gap:34px}
  .brand{display:flex;align-items:center;gap:6px}
  .brand__dot{width:36px;height:36px;border-radius:50%;background:var(--royal)}
  .brand__name{font-size:10.5px;font-weight:500;color:var(--royal);line-height:1.35;letter-spacing:.6px}
  .ea-badge{width:46px;height:28px;border:3px solid var(--badge)}

  .services{position:absolute;left:11px;right:34px;top:124px}
  .services .heading{font-size:12.5px}
  .sub{font-family:"Cinzel",serif;font-weight:700;color:var(--sub);font-size:8.8px;margin:13px 0 6px 8px}
  .services p{font-size:8.2px;line-height:1.42;margin-left:8px}
  .services p+p{margin-top:10px}
  .services .sub--get{margin-top:16px;margin-bottom:10px}
  .services .heading--books{font-size:11.5px;margin:14px 0 0 8px}
  .services .books-text{margin-top:10px}
</style>
</head>
<body>

<section class="page page--about">
  <svg class="page__art" viewBox="0 0 800 1130" preserveAspectRatio="none">
    <defs>
      <linearGradient id="deskPhoto" x1="0" y1="0" x2="1" y2="1">
        <stop offset="0" stop-color="#e8e4df"/>
        <stop offset=".6" stop-color="#efeeeb"/>
        <stop offset="1" stop-color="#d9b48c"/>
      </linearGradient>
    </defs>
    <rect class="photo" x="0" y="0" width="800" height="460" fill="url(#deskPhoto)" role="img" aria-label="Photo of a hand writing on tax forms at a desk"/>
    <path d="M800 0 L800 150 C560 160 260 270 0 430 L0 350 C250 210 550 70 800 0Z" fill="var(--royal)"/>
    <path d="M0 400 C220 270 460 190 640 160 C460 220 240 320 0 450Z" fill="var(--crimson)"/>
    <path d="M480 150 C620 130 720 140 800 170 L800 195 C720 170 610 160 480 150Z" fill="var(--crimson)"/>
    <path d="M0 220 C80 200 150 190 210 185 C140 205 70 235 0 265Z" fill="var(--crimson)"/>
    <path d="M0 272 C90 237 170 212 230 202 C160 237 80 277 0 322Z" fill="var(--royal)"/>
    <path d="M0 440 C200 300 480 210 800 200 L800 1130 L0 1130Z" fill="var(--paper)"/>
    <path d="M0 1060 C300 1040 600 960 800 830 L800 1130 L0 1130Z" fill="var(--royal)"/>
    <path d="M0 1130 C260 1080 540 1010 800 880 L800 920 C560 1030 320 1090 140 1130Z" fill="var(--crimson)"/>
    <path d="M0 1100 C120 1085 220 1070 300 1055 C200 1080 110 1105 40 1130 L0 1130Z" fill="var(--wine)"/>
  </svg>

  <div class="about">
    <h1 class="heading">About Maren T Holloway, MSA EA (Principal)</h1>
    <p class="about__text">I have a Masters' Degree in accounting and am an QDX Enrolled Agent. I am also a LedgerPro Advanced Certified Consultant in both the online and desktop products including Enterprise and Point of Sale. I provide individual and small business tax services, Accounting, bookkeeping, QDX representation, insurance audit representation, business license assistance and more.</p>
    <p class="about__text">I have experience working with a wide variety of clients from the point where they first decide they want to start a business. They are often unsure about what to do first- I have a lot of experience to offer you.</p>
  </div>

  <div class="brand-row">
    <div class="brand">
      <span class="brand__dot"></span>
      <span class="brand__name">MTH ACCOUNTING<br>&amp; CONSULTING, LLC</span>
    </div>
    <span class="ea-badge"></span>
  </div>
</section>

<section class="page page--services">
  <svg class="page__art" viewBox="0 0 800 1130" preserveAspectRatio="none">
    <path d="M0 0 L800 0 L800 340 L0 340Z" fill="var(--royal)"/>
    <path d="M0 140 C150 110 260 100 320 100 C220 120 120 150 0 190Z" fill="var(--crimson)"/>
    <path d="M190 0 L280 0 C480 110 660 220 800 290 L800 320 C640 230 420 110 190 0Z" fill="var(--wine)"/>
    <path d="M250 0 L400 0 C560 120 700 220 800 260 L800 340 C620 240 420 110 250 0Z" fill="var(--crimson)"/>
    <path d="M400 0 L530 0 C640 90 730 180 800 230 L800 260 C700 190 560 90 400 0Z" fill="var(--deep-blue)"/>
    <path d="M580 120 C670 150 740 170 800 190 L800 230 C730 200 650 160 580 120Z" fill="var(--crimson)"/>
    <path d="M0 180 C200 115 400 100 520 125 L800 330 L800 1130 L0 1130Z" fill="var(--paper)"/>
    <path d="M0 1130 L0 1020 C300 990 560 990 800 1010 L800 1130Z" fill="var(--royal)"/>
    <path d="M0 1050 C300 1030 560 1040 800 1060 L800 1130 L0 1130Z" fill="var(--deep-blue)"/>
  </svg>

  <div class="services">
    <h2 class="heading">What a Joy It Is to Watch Success in Action!</h2>

    <h3 class="sub">Tax Preparation – Why Hire Us?</h3>
    <p>Preparing your own income tax return can be a task that leaves you with more questions than answers. According to a study released by the National Tax Review Board last year, most taxpayers (77% of 71 million taxpayers) believe they benefited from using a professional tax preparer.<br>Whether we like it or not, today's tax laws are so complicated that filing a relatively simple return can be confusing. It is just too easy to overlook deductions and credits to which you are entitled. Even if you use a computer software program there's no substitute for the assistance of an experienced tax professional.</p>

    <h3 class="sub sub--get">Here's What Your Get...</h3>
    <p>Your tax return will be checked and rechecked by our computer software identifying potential problems the QDX may look at more closely and reviewing the math to limit QDX contacts.</p>
    <p>Your tax return can be filed electronically so you will get a refund back quicker.</p>
    <p>Our staff will show you how to adjust your payroll withholding to get more money back each week. Why give the QDX an interest free loan for up to 16 months.</p>
    <p>We will show you potential deductions to limit your tax liability for next year. In addition, we will give you a sheet of commonly overlooked deductions to limit the following year's tax liability.</p>

    <h2 class="heading heading--books">Books a Mess: No Problem!</h2>
    <p class="books-text">If you own a small business and haven't kept up your bookkeeping, don't worry. We can help you. We'll prepare your bookkeeping for the year, prepare a full Schedule C, as well as your personal income tax return. Then we'll help you set up an easy system that allows you to keep your books in tip-top shape next year.</p>
  </div>
</section>

</body>
</html>
```